Redesign Of Flower Delivery Subscription Service Website

I need a revamped website of www.petal-rush.com

Please revamp current design using same content....

Target Market(s)

people who buy flowers. Brides, wedding planners, wedding photographer, married man, boyfriend, etc.

Industry/Entity Type

Florist

Number of Pages Required

5+ page

Colors

Designer to choose colors to be used in the design.

Requirements
Must have
• I need a revamped website of www.petal-rush.com
• Please revamp current design using same content....
Nice to have
Should not have

```html
<!DOCTYPE html>
<html lang="en">
<head>
<meta charset="utf-8">
<title>Petal Rush – Monthly Flower Delivery</title>
<link rel="stylesheet" href="https://fonts.googleapis.com/css2?family=Lato:wght@400;700&family=Open+Sans:wght@400;600;700&display=swap">
<style>
:root{
  --mint:#4dcf9c;
  --pink:#e0437c;
  --leaf:#5aa51c;
  --teal:#3fc3c2;
  --ink:#333;
  --muted:#555;
  --footer:#ececec;
}
*{box-sizing:border-box;margin:0;padding:0}
html,body{width:1200px;height:5262px;overflow:hidden}
body{position:relative;background:#fff;font-family:"Lato",sans-serif;color:var(--ink)}
.abs{position:absolute}
a{color:inherit;text-decoration:none}

/* header */
.site-header{left:0;top:0;width:1200px;height:150px;background:#fff;box-shadow:0 2px 4px rgba(0,0,0,.06)}
.social{display:flex;gap:22px;align-items:center}
.social i{display:block;width:22px;height:22px;border-radius:50%;background:var(--teal)}
.brand{left:488px;top:14px;display:flex;align-items:center;gap:10px}
.brand .dot{width:18px;height:18px;border-radius:50%;background:var(--mint)}
.brand b{font:600 34px/1 "Open Sans",sans-serif;color:#555}
.brand small{position:absolute;left:28px;top:44px;font-size:10px;color:#777;white-space:nowrap}
.account{top:34px;display:flex;align-items:center;gap:8px;font-size:14px;color:#444}
.nav{left:84px;top:100px;display:flex;gap:38px;font-size:15px;color:#666}
.nav .active{color:var(--mint);position:relative}
.nav .active:after{content:"";position:absolute;left:0;right:0;top:30px;height:2px;background:var(--mint)}

/* hero */
.hero{left:0;top:150px;width:1200px;height:470px;background:linear-gradient(110deg,#e9c3c6 0%,#f3dcdd 35%,#e4b7bc 60%,#efd3d5 100%)}
.hero-frame{left:208px;top:240px;width:240px;height:275px;border:10px solid #fff;border-right:none}
.hero-title{left:255px;top:296px;font:700 56px/1 "Open Sans",sans-serif;color:var(--mint);letter-spacing:1px}
.hero-sub{left:255px;top:376px;font:600 26px/36px "Open Sans",sans-serif;color:#fff;text-shadow:0 1px 4px rgba(0,0,0,.45)}
.hero-sub em{font-style:normal;color:var(--pink);text-shadow:none}
.pill{display:inline-block;border-radius:18px;color:#fff;font:600 15px/32px "Open Sans",sans-serif;text-align:center}
.pills{left:478px;top:476px;display:flex;gap:26px}
.pills .teal{background:var(--teal);width:146px}
.pills .green{background:var(--leaf);width:150px}
.dots{left:544px;top:586px;display:flex;gap:14px}
.dots i{width:24px;height:3px;background:var(--pink)}

/* collection */
.collection{left:0;top:620px;width:1200px;height:862px;background:linear-gradient(180deg,#f8eef5,#f3eaf6 60%,#f7f2f8)}
.section-title{width:1200px;text-align:center;font:400 48px/1.1 "Open Sans",sans-serif}
.section-title .p{color:var(--pink)} .section-title .g{color:var(--mint)}
.card{top:785px;width:247px;height:565px;background:#fff;box-shadow:0 0 6px rgba(0,0,0,.08);text-align:center}
.card .photo{height:323px}
.card h3{margin:18px 16px 14px;font:400 15px/22px "Open Sans",sans-serif;color:var(--pink)}
.card p{margin:0 10px;font-size:11.5px;line-height:17px;color:var(--muted)}
.btn{display:block;background:var(--leaf);color:#fff;border-radius:18px;text-align:center;font:700 15px/34px "Open Sans",sans-serif;width:150px}

/* intro */
.intro-title{left:0;top:1540px;width:1200px;text-align:center;font:400 36px/50px "Open Sans",sans-serif}
.intro-title .g{color:var(--mint)} .intro-title .p{color:var(--pink)}
.intro-text{left:112px;top:1695px;width:976px;text-align:center;font-size:15px;line-height:24px;color:var(--ink)}

/* feature blocks */
.art-area{left:82px;width:1030px;background:linear-gradient(135deg,#fbe4dc 0%,#eef5ef 50%,#f6e2ec 100%)}
.feature{left:305px;width:605px;border:3px dashed #aaa;background:#fff;text-align:center;padding:46px 28px 0}
.feature h3{font:400 17px/25px "Open Sans",sans-serif;color:var(--pink);margin-bottom:28px}
.feature p{font-size:14.5px;line-height:23.5px;color:var(--muted)}

/* newsletter */
.newsletter{left:0;top:4640px;width:1200px;height:212px;background:linear-gradient(100deg,#f2f2f2 0%,#f6f6f6 60%,#cdeee8 85%,#eaf7f4 100%)}
.newsletter-title{left:0;top:4672px;width:1200px;text-align:center;font:600 30px/1 "Open Sans",sans-serif}
.newsletter-form{left:286px;top:4734px;display:flex}
.newsletter-form span{width:488px;height:52px;border:1px solid #ccc;border-right:none;border-radius:26px 0 0 26px;background:#fff;font-size:16px;line-height:50px;padding-left:28px;color:#888}
.newsletter-form b{width:140px;height:52px;background:var(--leaf);color:#fff;border-radius:0 26px 26px 0;text-align:center;font:700 18px/52px "Open Sans",sans-serif}

/* footer */
.footer{left:0;top:4852px;width:1200px;height:410px;background:var(--footer)}
.foot-h{top:4862px;font:400 32px/1 "Open Sans",sans-serif;color:var(--mint)}
.foot-h:after{content:"";display:block;width:20px;height:2px;background:var(--mint);margin-top:18px}
.about{left:112px;top:4940px;width:312px;font-size:14px;line-height:21px;color:#444}
.services{left:534px;top:4925px;list-style:none;font-size:14px;line-height:44px;color:#444}
.field{width:232px;height:34px;border:1px solid #ccc;border-radius:17px;background:#fff;font-size:13px;line-height:32px;padding-left:16px;color:#555}
.bottom{top:5230px;font-size:13px;color:#555}
</style>
</head>
<body>

<header class="site-header abs">
  <div class="social abs" style="left:82px;top:36px"><i></i><i></i><i></i><i></i><i></i></div>
  <div class="brand abs"><span class="dot"></span><b>Petal Rush</b><small>Coastal Flower Company</small></div>
  <div class="account abs" style="left:836px">
    <svg width="26" height="26" viewBox="0 0 26 26"><circle cx="13" cy="13" r="13" fill="#3e8dd8"/><circle cx="13" cy="10" r="5" fill="#fff"/><path d="M4 22a9 7 0 0 1 18 0z" fill="#fff"/></svg>My Account
  </div>
  <div class="account abs" style="left:1000px">
    <svg width="32" height="26" viewBox="0 0 32 26"><path d="M1 3h6l4 14h16l3-10H9" fill="none" stroke="#3e8dd8" stroke-width="3"/><circle cx="13" cy="22" r="2.5" fill="#3e8dd8"/><circle cx="25" cy="22" r="2.5" fill="#3e8dd8"/></svg>Buy Now
  </div>
  <nav class="nav abs">
    <a class="active">Home</a><a>How it Works</a><a>Delivery Areas</a><a>Franchise</a><a>Blog</a><a>Free Flowers Monthly</a><a>Corporate Arrangements</a><a>Help</a>
  </nav>
</header>

<section class="hero abs" role="img" aria-label="Soft-focus photograph of pale pink blossoms"></section>
<div class="hero-frame abs"></div>
<h1 class="hero-title abs">ALWAYS FRESH</h1>
<p class="hero-sub abs">Beautiful Flower Arrangements Delivered<br>Monthly Now only <em>$69.95/MTH</em> ($100 value)</p>
<div class="pills abs"><span class="pill teal">Free Vase</span><span class="pill green">Free Delivery</span><span class="pill green">Free Upgrade</span></div>
<div class="dots abs"><i></i><i></i><i></i></div>

<section class="collection abs"></section>
<h2 class="section-title abs" style="left:0;top:658px"><span class="p">Spark of</span> <span class="g">Our Collection</span></h2>

<article class="card abs" style="left:86px">
  <div class="photo" role="img" aria-label="Purple roses and lilies in a glass vase" style="background:linear-gradient(180deg,#6b4a7e,#9b6fa3 50%,#5a4a3e)"></div>
  <h3>SET IT AND FORGET IT</h3>
  <p>Petal Rush is a "SET IT AND FORGET IT" subscription based flower delivery service. For an Amazing price Petal Rush will hand deliver a gorgeous arrangement directly to anyone you want every month without you having to worry about it.</p>
</article>
<article class="card abs" style="left:347px">
  <div class="photo" role="img" aria-label="Cream and peach roses in a clear vase" style="background:linear-gradient(180deg,#efe6df,#e8cdb8 55%,#d9d2c9)"></div>
  <h3>BUT NEVER FORGET<br>AGAIN</h3>
  <p>When setting up your account, you can choose exact delivery dates for the months that have special days such as your Anniversary, Birthday, Valentines Day and Mothers Day. You might forget but we won't, we have got ya covered!</p>
</article>
<article class="card abs" style="left:607px">
  <div class="photo" role="img" aria-label="White and pink hydrangea bouquet against a blue sky" style="background:linear-gradient(180deg,#3b8fd6,#b9d6ee 45%,#e9e2ea 75%,#9fc7e3)"></div>
  <h3>MAKING SOMEONE'S<br>DAY BETTER</h3>
  <p>Petal Rush is a "SET IT AND FORGET IT" subscription based flower delivery service. For an Amazing price Petal Rush will hand deliver a gorgeous arrangement directly to anyone you want every month without you having to worry about it.</p>
</article>
<article class="card abs" style="left:868px">
  <div class="photo" role="img" aria-label="Coral roses with greenery in a red vase" style="background:linear-gradient(180deg,#fff,#f6c3ae 45%,#e98a74 70%,#f5f0ee)"></div>
  <h3>SET IT AND FORGET IT</h3>
  <p>Be the hero in that special someone's life each and every month.<br><br>It feels good to make a difference in your loved ones day.</p>
</article>
<a class="btn abs" style="left:525px;top:1396px">View More</a>

<h2 class="intro-title abs"><span class="g">Monthly Subscription Based Flower Delivery Service</span><br><span class="p">in San Diego – CA by Our Florist Shop</span></h2>
<p class="intro-text abs">Every moment of life could be cherished perfectly.......IF you choose wisely. To make your day more treasured, remember that flowers are the smartest choice when delivered through our monthly Petal Rush subscription based delivery service. Our online subscription-based flower delivery service can help you pamper, cherish and make an everlasting impression on the minds of your loved ones with a doorstep delivery of exquisitely hand-designed floral arrangements. Our online subscription service features both standard and personalized services to help you choose from an assortment of classic and contemporary floral arrangements. It is your chance to setup a weekly, monthly, or quarterly subscription, so we can deliver the most exotic collections of hand-decorated flowers that you and your loved ones will cherish.</p>

<div class="art-area abs" style="top:1880px;height:830px" role="img" aria-label="Watercolour wreath of tropical flowers, leaves and berries framing the text"></div>
<div class="feature abs" style="top:2077px;height:483px">
  <h3>Exotic Flowers Garnished With Special Hues To<br>Compliment Your Loved Ones</h3>
  <p>Let's not forget a single day in which you can make your loved ones feel special. Whether it's your anniversary or a birthday in your family, you must always go an extra mile to show "how much I care about you." Nothing can compare to your show of love, or compliment the joy of your loved ones, more than a perfectly blossomed bouquet of flowers. So if you are having difficulty in finding the perfect flower bouquet to share your overflowing love with that special person, don't worry......Petal Rush has got it all covered for you! We believe that our hand-picked and hand-designed flowers, created with a combination of lavish designs and feminine hues, will definitely grab the attention of your loved ones. At Petal Rush, we deliver both birthday flowers and sympathy flowers garnished with special hues of love and support. Our bouquets share your side of affection and sorrow with your loved ones on any memorable day of their lives.</p>
</div>

<div class="art-area abs" style="top:2745px;height:830px" role="img" aria-label="Watercolour wreath of tropical flowers, leaves and berries framing the text"></div>
<div class="feature abs" style="top:2935px;height:475px">
  <h3>Standard And Personalized Flower Arrangements<br>For Special Occasions</h3>
  <p>Petal Rush offers on time subscription based service that is risk free, trouble free and affordable at the same time. We offer the most trusted and delightful flower delivery service in San Diego, and are designed to deliver your desired floral arrangements within your requested days and times. Our local florists will happily take your orders online for your shopping convenience. You can count on us to deliver fresh flower baskets and bouquets for birthdays, weddings, mother's day, anniversaries and other special events within your locality, and even across the country. In case you're looking for something personalized, then our skilled florists can create custom arrangements for any special occasion. Get Yourself Subscribed And Claim Discounts On Big Orders!</p>
</div>

<div class="art-area abs" style="top:3610px;height:830px" role="img" aria-label="Watercolour wreath of tropical flowers, leaves and berries framing the text"></div>
<div class="feature abs" style="top:3790px;height:540px">
  <h3>Get Yourself Subscribed And Claim Discounts On<br>Big Orders!</h3>
  <p>Get love and adulation by gifting flowers to your loved ones on those special occasions. Whether it's formal, personal or your love for your family, just follow the subscription criteria and get your hands on the most valuable service for all kinds of events, occasions and parties. Set up your account and select the right delivery dates for the special months and leave the rest to us. We will deliver your flowers on the exact special dates to make your loved one's day wonderful. It is your chance to experience the simple, risk-free and trouble-free delivery of flowers right to the doorstep of your cherished loved</p>
</div>
<a class="btn abs" style="left:525px;top:4524px">View All</a>

<section class="newsletter abs"></section>
<h2 class="newsletter-title abs"><span style="color:var(--leaf)">Enter Your Email To</span>&nbsp; <span style="color:var(--pink)">Receive A Free Upgrade</span></h2>
<div class="newsletter-form abs"><span>Your e-mail address</span><b>Submit</b></div>

<footer class="footer abs"></footer>
<h3 class="foot-h abs" style="left:112px">About Us</h3>
<h3 class="foot-h abs" style="left:534px">More Services</h3>
<h3 class="foot-h abs" style="left:880px">Get In Touch</h3>
<p class="about abs">Lorem Ipsum is simply dummy text of the printing and typesetting industry. Lorem Ipsum has been the industry's standard dummy text ever since the 1500s, when an unknown printer took a galley of type and scrambled it to make a type specimen book. It has survived not only five centuries, but also the leap into electronic typesetting, remaining essentially unchanged.</p>
<ul class="services abs"><li>Corporate Arrangements</li><li>Hotel Arrangements</li><li>Events</li><li>Weddings</li></ul>
<div class="field abs" style="left:858px;top:4918px">E-mail</div>
<div class="field abs" style="left:858px;top:4982px">Subject</div>
<div class="field abs" style="left:904px;top:5044px;width:142px;text-align:center;padding:0">Submit</div>
<div class="social abs" style="left:848px;top:5148px;gap:34px"><i></i><i></i><i></i><i></i><i></i></div>
<p class="bottom abs" style="left:114px">Copyright 2018. All Rights Reserved by Petal Rush - Monthly Flowers Delivery.</p>
<p class="bottom abs" style="left:834px">Privacy Policy &nbsp;&nbsp;&nbsp;&nbsp; Terms &amp; Conditions</p>

</body>
</html>
```